Luxury Lifestyle service requires name card

Logo of my company has to be on the left side of the card. (Blue logo)Name and information preferably on the right side.QR code inclusion would be great , Gold logo if it can be included at the back of the card would be great too- we are a luxury lifestyle concierge company catering to the high net worth clients.

Target Market(s)

high net worth customers / luxury

Industry/Entity Type

Business Service

Contact Information for Business Card

name
contact
email
website

Font styles to use
Serif

Colors
0255a3
3176b5
85abd2
0492cd
33a6d7
85cae6
cee9f5

Requirements
Must have
• Logo of my company has to be on the left side of the card. (Blue logo)
• Name and information on the right side.
Nice to have
• QR code inclusion would be great
Should not have
• Do not use colours :- red , purple , orange , yellow
• background card colour : do not use black

```html
<!DOCTYPE html>
<html lang="en">
<head>
<meta charset="utf-8">
<title>Lumera Daily – Business Card</title>
<link rel="stylesheet" href="https://fonts.googleapis.com/css2?family=Open+Sans:wght@300;400&display=swap">
<style>
  :root {
    --backdrop: #bddcba;
    --card-white: #ffffff;
    --ink: #3a3a3a;
    --brand-blue: #0492cd;
    --accent-blue: #33a6d7;
    --icon-blue: #0255a3;
    --back-center: #2a80c2;
    --back-edge: #1c578c;
    --mark-white: #ffffff;
  }
  * { margin: 0; padding: 0; box-sizing: border-box; }
  html, body {
    width: 1200px; height: 1200px; overflow: hidden;
    background: var(--backdrop);
    font-family: "Open Sans", sans-serif;
  }
  .canvas {
    position: relative; width: 1200px; height: 1200px;
    display: flex; align-items: center; justify-content: center; gap: 44px;
  }
  .card {
    position: relative; width: 540px; height: 309px;
    box-shadow: 0 10px 24px rgba(40, 70, 40, 0.18);
  }
  .card-front { background: var(--card-white); }
  .brand {
    position: absolute; left: 46px; top: 40px;
    display: flex; align-items: center; gap: 12px;
  }
  .brand-dot {
    width: 30px; height: 30px; border-radius: 50%;
    background: var(--accent-blue);
  }
  .brand-name {
    font-weight: 300; font-size: 21px; letter-spacing: 1px;
    color: var(--ink);
  }
  .contact {
    position: absolute; right: 46px; bottom: 36px;
    width: 210px;
  }
  .contact-name {
    font-weight: 400; font-size: 21px; color: var(--brand-blue);
    margin-bottom: 8px;
  }
  .contact-line {
    display: flex; align-items: center; gap: 8px;
    font-size: 14.5px; color: var(--ink); line-height: 22px;
  }
  .contact-line svg { width: 11px; height: 11px; flex: none; fill: var(--icon-blue); }
  .card-back {
    background: radial-gradient(circle at 55% 40%, var(--back-center), var(--back-edge) 75%);
    display: flex; align-items: center; justify-content: center;
  }
  .back-mark {
    display: flex; flex-direction: column; align-items: center; gap: 14px;
  }
  .back-ring {
    width: 120px; height: 120px; border-radius: 50%;
    border: 3px solid var(--mark-white);
  }
  .back-name {
    font-weight: 300; font-size: 20px; letter-spacing: 2px;
    color: var(--mark-white);
  }
</style>
</head>
<body>
  <main class="canvas">
    <section class="card card-front" aria-label="Card front">
      <div class="brand">
        <span class="brand-dot"></span>
        <span class="brand-name">LUMERA DAILY</span>
      </div>
      <div class="contact">
        <p class="contact-name">John Doe</p>
        <p class="contact-line">
          <svg viewBox="0 0 12 12" aria-hidden="true"><path d="M2.5 1h2l1 2.5-1.3 1a6 6 0 0 0 3.3 3.3l1-1.3L11 7.5v2A1.5 1.5 0 0 1 9.5 11 8.5 8.5 0 0 1 1 2.5 1.5 1.5 0 0 1 2.5 1z"/></svg>
          +63 900 555 0142
        </p>
        <p class="contact-line">
          <svg viewBox="0 0 12 12" aria-hidden="true"><path d="M1 2.5h10v7H1z M1.5 3l4.5 3.5L10.5 3" fill="none" stroke="#0255a3" stroke-width="1.2"/></svg>
          john@lumeraday.com
        </p>
        <p class="contact-line">
          <svg viewBox="0 0 12 12" aria-hidden="true"><circle cx="6" cy="6" r="4.8" fill="none" stroke="#0255a3" stroke-width="1.1"/><path d="M1.2 6h9.6M6 1.2c-2.4 2.6-2.4 7 0 9.6M6 1.2c2.4 2.6 2.4 7 0 9.6" fill="none" stroke="#0255a3" stroke-width="0.9"/></svg>
          www.lumeraday.com
        </p>
      </div>
    </section>

    <section class="card card-back" aria-label="Card back">
      <div class="back-mark">
        <span class="back-ring"></span>
        <span class="back-name">LUMERA DAILY</span>
      </div>
    </section>
  </main>
</body>
</html>
```